Marketing Email Design - to be reused with new content on an ongoing basis

Create a marketing email template based on the product current design - this email will be updated with content and sent to customers on a continual basis so it needs to account for placeholders etc within its design whereby the updates and content of new release or information releases will be included continually - it is aimed to take the HTML template and design and utilise it within a salesforce continuing marketing campaign to be friendly with all standard email applications and mobile devices for rendering - design and color scheme to follow the Corvane Q Logo and teldunsoft logos

hi res logos will be provided

Target Market(s)

Multiple this will be sent to all current customers on a continual basis to promote the product / enhancements and new releases

Industry/Entity Type

Business Software

Requirements
Must have
• Must be compatible with all major email applications
• Must be mobile device compatible
• Must be inspired colour scheme and fonts to compliment the current logos and easy of reading
Nice to have
• Placeholders and sections for updating for subsequent email campaigns easily
• Attractive and eye catching so that users will actually read the content and not instantly dismiss

```html
<!DOCTYPE html>
<html lang="en">
<head>
<meta charset="utf-8">
<title>Corvane Q – Product Update Email</title>
<link rel="stylesheet" href="https://fonts.googleapis.com/css2?family=Cinzel:wght@500;700&family=Open+Sans:wght@400;600;700&family=Oswald:wght@500;600&display=swap">
<style>
  :root {
    --page-bg: #f3f4f6;
    --navy: #1d3557;
    --navy-deep: #14243d;
    --band-blue: #2b5189;
    --band-blue-dark: #203f6e;
    --accent-red: #d3222a;
    --accent-red-dark: #a9161d;
    --accent-orange: #ef7b1e;
    --highlight-yellow: #f6c344;
    --text-dark: #3b3b3b;
    --text-muted: #6a6a6a;
    --white: #ffffff;
  }
  * { box-sizing: border-box; margin: 0; padding: 0; }
  html, body { width: 1200px; height: 2280px; overflow: hidden; }
  body {
    background: var(--page-bg);
    font-family: "Open Sans", Arial, sans-serif;
    color: var(--text-dark);
    position: relative;
  }
  a { color: inherit; }

  .preheader {
    height: 60px; line-height: 60px; text-align: center;
    font-size: 18px; color: var(--text-dark);
  }
  .preheader a { font-weight: 700; }

  .email { width: 1000px; margin: 0 auto; background: var(--white); box-shadow: 0 0 18px rgba(0,0,0,.12); }

  /* hero */
  .hero { position: relative; height: 540px; border-top: 8px solid var(--accent-red); overflow: hidden; }
  .hero-photo {
    position: absolute; inset: 0;
    background:
      linear-gradient(180deg, rgba(20,36,61,.95) 0%, rgba(29,53,87,.85) 22%, rgba(29,53,87,0) 34%),
      radial-gradient(ellipse at 55% 65%, #f4f2ee 0%, #dcd8d2 45%, #b9b3ab 80%, #8e8881 100%);
  }
  .brand-bar { position: absolute; top: 28px; left: 0; right: 0; height: 92px; display: flex; justify-content: space-between; align-items: center; padding: 0 0 0 36px; }
  .brand-primary { font-size: 54px; font-weight: 600; color: var(--white); letter-spacing: -1px; }
  .brand-partner {
    background: var(--accent-red); color: var(--white);
    font-size: 44px; font-weight: 600; height: 92px; line-height: 92px;
    padding: 0 40px 0 60px; clip-path: polygon(12% 0, 100% 0, 100% 100%, 0 100%);
  }
  .hero-tagline {
    position: absolute; left: 0; right: 0; bottom: 28px; height: 132px;
    background: rgba(255,255,255,.72);
    display: flex; align-items: center; justify-content: center; text-align: center;
    font-family: "Cinzel", Georgia, serif; font-weight: 700; font-size: 36px; line-height: 1.15;
    color: var(--navy);
  }

  /* intro band */
  .intro {
    position: relative; height: 340px;
    background: linear-gradient(180deg, var(--band-blue) 0%, var(--band-blue-dark) 100%);
    text-align: center; padding: 40px 80px 0;
  }
  .intro-text {
    font-family: "Cinzel", Georgia, serif; font-weight: 500;
    color: var(--white); font-size: 27px; line-height: 1.28;
  }
  .intro-text strong { color: var(--highlight-yellow); font-weight: 700; }
  .cta-button {
    display: inline-block; margin-top: 34px;
    background: linear-gradient(180deg, #e03a3f 0%, var(--accent-red-dark) 100%);
    color: var(--white); text-decoration: none;
    font-family: "Oswald", Arial, sans-serif; font-weight: 600; font-size: 42px;
    height: 88px; line-height: 88px; padding: 0 46px; border-radius: 6px;
    box-shadow: 0 4px 10px rgba(0,0,0,.35);
  }
  .intro-pointer { position: absolute; left: 460px; bottom: -40px; width: 80px; height: 40px; }

  /* features */
  .features { display: flex; padding: 80px 40px 40px; gap: 40px; height: 500px; }
  .feature { flex: 1; }
  .feature-icon { height: 140px; margin-bottom: 24px; display: flex; align-items: center; }
  .feature-title { font-family: "Open Sans", Arial, sans-serif; font-weight: 700; font-size: 24px; color: var(--accent-orange); margin-bottom: 18px; line-height: 1.2; }
  .feature-body { font-size: 19px; line-height: 1.4; color: var(--text-muted); margin-bottom: 18px; }
  .read-more {
    display: inline-block; background: var(--accent-red); color: var(--white); text-decoration: none;
    font-weight: 600; font-size: 17px; padding: 4px 20px; border-radius: 14px;
  }
  .map-block {
    width: 220px; height: 130px; border-radius: 6px;
    background: radial-gradient(ellipse at 50% 50%, #8fb2d9 0%, #c9dbef 60%, #ffffff 100%);
  }

  /* second photo */
  .feature-photo { position: relative; height: 340px; overflow: hidden; }
  .feature-photo-fill {
    position: absolute; inset: 0;
    background: linear-gradient(120deg, #6f7e8c 0%, #b9c2ca 40%, #e7e9ea 65%, #9aa3aa 100%);
  }
  .feature-photo-caption {
    position: absolute; left: 0; right: 0; top: 150px; height: 90px;
    background: rgba(255,255,255,.7);
    display: flex; align-items: center; justify-content: center;
    font-family: "Cinzel", Georgia, serif; font-weight: 500; font-size: 44px; color: var(--navy);
  }

  /* footer */
  .footer { background: var(--navy-deep); height: 180px; color: var(--white); }
  .footer-company { text-align: center; padding-top: 28px; font-size: 15px; line-height: 1.5; color: #c9d3e3; }
  .footer-contact { display: flex; align-items: center; padding: 28px 36px 0; gap: 24px; font-size: 15px; }
  .contact-item { display: flex; align-items: center; gap: 8px; }
  .contact-item svg { width: 30px; height: 30px; }
  .social { margin-left: auto; display: flex; gap: 14px; }
  .social span { width: 50px; height: 50px; border-radius: 50%; background: var(--white); display: block; }

  .legal { text-align: center; font-size: 16px; color: var(--text-dark); line-height: 1.5; }
  .legal-copyright { padding-top: 30px; }
  .legal-unsubscribe { padding-top: 40px; }
  .legal a { font-weight: 600; }
</style>
</head>
<body>
  <p class="preheader">Can’t see message below? <a href="#">Click here</a> to view in your browser.</p>

  <main class="email">
    <header class="hero">
      <div class="hero-photo" role="img" aria-label="Photo of business people's hands reviewing charts on paper at a meeting table"></div>
      <div class="brand-bar">
        <span class="brand-primary">Corvane</span>
        <span class="brand-partner">teldunsoft</span>
      </div>
      <h1 class="hero-tagline">We provide our clients with<br>an independent, secure, and<br>scalable platform</h1>
    </header>

    <section class="intro">
      <p class="intro-text">Using our <strong>universal thin client interface</strong>, customers can view and analyze their data regardless of source type, data type or physical location of their storage systems.</p>
      <a class="cta-button" href="#">CLICK HERE TO SUBSCRIBE</a>
      <svg class="intro-pointer" viewBox="0 0 80 40" aria-hidden="true"><polygon points="0,0 80,0 40,40" fill="#203f6e"/></svg>
    </section>

    <section class="features">
      <article class="feature">
        <div class="feature-icon">
          <svg width="220" height="130" viewBox="0 0 220 130" aria-hidden="true">
            <circle cx="55" cy="65" r="50" fill="#d7dde5"/>
            <rect x="130" y="20" width="80" height="90" rx="6" fill="#ef7b1e"/>
          </svg>
        </div>
        <h2 class="feature-title">HTML5 PLATFORM</h2>
        <p class="feature-body">Develop Once, Deploy everywhere. No additional costs to deploy to Pryxa, Pryxa Tab, Droplet, Quorra phone platforms. No proprietary apps needed!</p>
        <a class="read-more" href="#">Read More »</a>
      </article>
      <article class="feature">
        <div class="feature-icon">
          <svg width="220" height="130" viewBox="0 0 220 130" aria-hidden="true">
            <rect x="10" y="20" width="180" height="90" rx="6" fill="#6aa6db"/>
          </svg>
        </div>
        <h2 class="feature-title">KSS INTEGRATION</h2>
        <p class="feature-body">Enterprise platform plus single sign-on make this a robust and convenient application</p>
        <a class="read-more" href="#">Read More »</a>
      </article>
      <article class="feature">
        <div class="feature-icon">
          <div class="map-block" role="img" aria-label="World map with connected network points"></div>
        </div>
        <h2 class="feature-title">SCALABLE<br>ARCHITECTURE</h2>
        <p class="feature-body">Including automated load balancing across horizontal/vertical architecture through much improved performance and reliability.</p>
        <a class="read-more" href="#">Read More »</a>
      </article>
    </section>

    <section class="feature-photo">
      <div class="feature-photo-fill" role="img" aria-label="Photo of a laptop with charts on a desk beside a window"></div>
      <h2 class="feature-photo-caption">DATA IS OUR BUSINESS</h2>
    </section>

    <footer class="footer">
      <p class="footer-company">Harlow Integration Ltd. IT &amp; IT Communications &amp; Software Consultants<br>Kilbrook, Co. Marran, Ireland</p>
      <div class="footer-contact">
        <span class="contact-item">
          <svg viewBox="0 0 30 30" aria-hidden="true"><circle cx="15" cy="15" r="15" fill="#fff"/><path d="M10 8 l3 0 l1.5 4 l-2 1.5 a9 9 0 0 0 4 4 l1.5 -2 l4 1.5 l0 3 a2 2 0 0 1 -2 2 a14 14 0 0 1 -12 -12 a2 2 0 0 1 2 -2z" fill="#14243d"/></svg>
          +353 (0)51 555 0142
        </span>
        <span class="contact-item">
          <svg viewBox="0 0 30 30" aria-hidden="true"><circle cx="15" cy="15" r="15" fill="#fff"/><circle cx="15" cy="15" r="8" fill="none" stroke="#14243d" stroke-width="2"/><path d="M7 15 h16 M15 7 v16" stroke="#14243d" stroke-width="1.6"/></svg>
          www.harlowintegration.com
        </span>
        <span class="contact-item">
          <svg viewBox="0 0 30 30" aria-hidden="true"><circle cx="15" cy="15" r="15" fill="#fff"/><rect x="7" y="10" width="16" height="11" fill="none" stroke="#14243d" stroke-width="2"/><path d="M7 10 l8 6 l8 -6" fill="none" stroke="#14243d" stroke-width="2"/></svg>
          info@harlowintegration.com
        </span>
        <span class="social" aria-label="Social links"><span></span><span></span><span></span></span>
      </div>
    </footer>
  </main>

  <p class="legal legal-copyright">Copyright © 2014 Harlow Integration Ltd. All rights reserved.<br><a href="#">Terms of Use</a> | <a href="#">Privacy Policy</a></p>
  <p class="legal legal-unsubscribe">You are receiving this email because you subscribed at www.harlowintegration.com. <a href="#">Click here</a> to unsubscribe.</p>
</body>
</html>
```